" Temos como objetivo melhor atender as demandas atuais em TI com suporte de fácil acesso e analistas especializados com certificações que o mercado atual exige. Nossa equipe se dedica à prevenção, resolução de problemas e sugestões de melhorias do ambiente para garantir que seus servidores e aplicações estejam sempre no ar e funcionando, garantindo a continuidade dos negócios, foco das nossas soluções. "

```html
<!DOCTYPE html>
<html lang="en">
<head>
<meta charset="UTF-8">
<title>Servix Email Signature</title>
<link rel="stylesheet" href="https://fonts.googleapis.com/css2?family=Montserrat:wght@400;500;600&display=swap">
<style>
  :root {
    --bg-orange: #ff6a00;
    --navy: #0e2a47;
    --white: #ffffff;
    --accent-orange: #ff7a00;
    --accent-yellow: #ffc21a;
    --brand-ink: #1c2f4a;
    --text-light: #dfe6ee;
  }
  * { margin: 0; padding: 0; box-sizing: border-box; }
  html, body { width: 1200px; height: 1200px; overflow: hidden; }
  body {
    background: var(--bg-orange);
    font-family: "Montserrat", sans-serif;
    position: relative;
  }
  .signature { position: absolute; left: 0; top: 0; width: 1200px; height: 1200px; }
  .signature-shapes { position: absolute; left: 0; top: 0; }
  .brand {
    position: absolute; left: 228px; top: 564px; height: 54px;
    display: flex; align-items: center; gap: 12px;
  }
  .brand-dot { width: 36px; height: 36px; border-radius: 50%; background: var(--accent-orange); }
  .brand-name {
    font-size: 38px; font-weight: 500; letter-spacing: 5px; color: var(--brand-ink);
  }
  .person { position: absolute; left: 655px; top: 549px; }
  .person-name { font-size: 14px; font-weight: 500; color: var(--white); line-height: 16px; }
  .person-role { font-size: 11px; font-weight: 500; color: var(--accent-yellow); line-height: 14px; }
  .contact {
    position: absolute; display: flex; align-items: center; gap: 12px;
    font-size: 9px; color: var(--text-light);
  }
  .contact svg { width: 14px; height: 14px; flex: none; }
  .contact-address { left: 657px; top: 591px; }
  .contact-phone { left: 657px; top: 617px; }
  .contact-email { left: 826px; top: 591px; }
  .contact-web { left: 826px; top: 617px; }
  .social { position: absolute; left: 654px; top: 643px; display: flex; gap: 27px; }
  .social-item { width: 13px; height: 13px; border-radius: 50%; background: var(--white); }
</style>
</head>
<body>
<main class="signature">
  <svg class="signature-shapes" width="1200" height="1200" viewBox="0 0 1200 1200" aria-hidden="true">
    <defs>
      <linearGradient id="swoosh" x1="0" y1="0" x2="1" y2="1">
        <stop offset="0" stop-color="var(--accent-yellow)"/>
        <stop offset="1" stop-color="var(--accent-orange)"/>
      </linearGradient>
    </defs>
    <path class="panel-white" d="M151,509 H625 V691 H241 A90,90 0 0 1 151,601 Z" fill="var(--white)"/>
    <path class="panel-swoosh" d="M528,509 H560 C592,560 610,630 619,691 H584 C574,620 560,560 528,509 Z" fill="url(#swoosh)"/>
    <path class="panel-swoosh-light" d="M528,509 H540 C566,560 578,630 584,691 H578 C568,620 552,560 528,509 Z" fill="var(--accent-yellow)"/>
    <path class="panel-navy" d="M557,509 H989 A60,60 0 0 1 1049,569 V691 H619 C608,620 590,560 557,509 Z" fill="var(--navy)"/>
  </svg>

  <div class="brand">
    <span class="brand-dot"></span>
    <span class="brand-name">SERVIX</span>
  </div>

  <div class="person">
    <p class="person-name">Name</p>
    <p class="person-role">Project Manager</p>
  </div>

  <div class="contact contact-address">
    <svg viewBox="0 0 14 14"><path d="M7 1a4 4 0 0 1 4 4c0 3-4 8-4 8S3 8 3 5a4 4 0 0 1 4-4z" fill="var(--accent-yellow)"/><circle cx="7" cy="5" r="1.5" fill="var(--navy)"/></svg>
    <span>Harbor 218 Avenue NY USA</span>
  </div>
  <div class="contact contact-phone">
    <svg viewBox="0 0 14 14"><path d="M3 1.5l2.5 0 1 3-1.5 1.2a7 7 0 0 0 3.3 3.3L9.5 7.5l3 1V11a1.5 1.5 0 0 1-1.5 1.5A9.5 9.5 0 0 1 1.5 3 1.5 1.5 0 0 1 3 1.5z" fill="var(--accent-yellow)"/></svg>
    <span>+100 5550 123</span>
  </div>
  <div class="contact contact-email">
    <svg viewBox="0 0 14 14"><rect x="1.5" y="3" width="11" height="8" rx="1" fill="var(--accent-yellow)"/><path d="M1.5 3.5 7 8l5.5-4.5" stroke="var(--navy)" stroke-width="1" fill="none"/></svg>
    <span>contact@servixmail.com</span>
  </div>
  <div class="contact contact-web">
    <svg viewBox="0 0 14 14"><rect x="4" y="1" width="6" height="12" rx="1.2" fill="var(--accent-yellow)"/><rect x="5.2" y="2.5" width="3.6" height="7.5" fill="var(--navy)"/></svg>
    <span>www.servixsite.com</span>
  </div>

  <div class="social" aria-label="Social links">
    <span class="social-item"></span>
    <span class="social-item"></span>
    <span class="social-item"></span>
    <span class="social-item"></span>
  </div>
</main>
</body>
</html>
```